Postcard Design

Bluestone Haven Group Company Inc, is a air duct cleaning, dryer vent cleaning & pressure washing company, we would like this postcard to focus fully on our pressure washing specials for the season.

```html
<!DOCTYPE html>
<html lang="en">
<head>
<meta charset="utf-8">
<title>Bluestone Haven Group – Pressure Washing Postcard</title>
<link rel="stylesheet" href="https://fonts.googleapis.com/css2?family=Arimo:ital,wght@0,400;0,700;1,400;1,700&family=Fredoka:wght@600&family=Oswald:wght@500&family=Alfa+Slab+One&display=swap">
<style>
  :root {
    --page: #ffffff;
    --sky-top: #1e8fe6;
    --sky-mid: #6cc0f2;
    --sky-low: #bfe3f7;
    --grass-top: #7cc23a;
    --grass-low: #4f9a22;
    --ink: #1d2633;
    --ink-soft: #2b2f36;
    --teal: #1f9fb0;
    --teal-dark: #1b6e74;
    --tag: #e4f07a;
    --blue-band: #3a93ee;
    --blue-text: #2a9ae6;
    --blue-card-top: #a9d3ef;
    --blue-card-low: #d9ecf8;
    --coupon-fill: #e3f1fb;
    --coupon-title: #f2c52a;
    --coupon-teal: #12806f;
    --label-yellow: #f5f26a;
  }
  * { box-sizing: border-box; margin: 0; padding: 0; }
  html, body { width: 1061px; height: 1200px; overflow: hidden; background: var(--page); }
  body { position: relative; font-family: "Arimo", Arial, sans-serif; }

  .card { position: absolute; overflow: hidden; box-shadow: 0 3px 8px rgba(0,0,0,.45); }
  .card--front { left: 29px; top: 29px; width: 1004px; height: 550px;
    background: linear-gradient(180deg, var(--sky-top) 0%, var(--sky-mid) 45%, var(--sky-low) 72%, var(--grass-top) 78%, var(--grass-low) 100%); }
  .card--back { left: 29px; top: 620px; width: 1005px; height: 553px;
    background: linear-gradient(160deg, var(--blue-card-top) 0%, var(--blue-card-low) 55%, var(--blue-card-top) 100%); }

  .abs { position: absolute; white-space: nowrap; }

  .brand { display: flex; align-items: center; gap: 9px; color: var(--teal); font-weight: 700; white-space: nowrap; }
  .brand__dot { border-radius: 50%; background: var(--teal); flex: none; }

  /* front */
  .front-brand { left: 46px; top: 66px; font-size: 36px; }
  .front-brand .brand__dot { width: 20px; height: 20px; }
  .front-web { left: 88px; top: 160px; font-size: 16px; font-weight: 700; color: var(--ink-soft); letter-spacing: .3px; }
  .front-phone { left: 439px; top: 78px; font-size: 36px; font-weight: 700; color: var(--ink); }
  .front-call { left: 749px; top: 86px; font-size: 27px; font-style: italic; font-weight: 700; color: var(--ink); }
  .front-areas { left: 439px; top: 135px; font-size: 18px; font-style: italic; color: var(--ink); line-height: 25px; }
  .services-title { left: 128px; top: 220px; font-family: "Fredoka", Arial, sans-serif; font-size: 22px; font-variant: small-caps; color: var(--ink); letter-spacing: .5px; }
  .services-list { left: 131px; top: 258px; list-style: none; font-family: "Fredoka", Arial, sans-serif; font-size: 16px; color: var(--ink); }
  .services-list li { height: 23.4px; display: flex; align-items: center; gap: 10px; }
  .services-list li::before { content: ""; width: 11px; height: 13px; border-radius: 50%; background: #111; }
  .services-list li.more { padding-left: 42px; }
  .services-list li.more::before { display: none; }
  .house-photo { left: 362px; top: 192px; width: 640px; height: 282px;
    background: linear-gradient(180deg, #4d5560 0%, #e9eef2 35%, #f4f6f7 70%, #3b7a2a 100%); border-radius: 4px; }
  .tagline { left: 0; right: 0; top: 496px; text-align: center; padding-left: 120px; font-size: 33px; font-style: italic; font-weight: 700; color: var(--tag); text-shadow: 0 1px 2px rgba(0,0,0,.35); }

  /* back */
  .back-brand { left: 40px; top: 44px; font-size: 27px; }
  .back-brand .brand__dot { width: 16px; height: 16px; }
  .back-web { left: 331px; top: 35px; font-size: 13px; color: var(--ink-soft); }
  .back-phone { left: 338px; top: 54px; font-size: 33px; color: var(--teal-dark); }
  .back-call { left: 362px; top: 92px; font-size: 22px; font-weight: 700; color: var(--blue-text); letter-spacing: .5px; }
  .back-services { left: 37px; top: 124px; font-family: "Oswald", Arial, sans-serif; font-size: 19px; color: var(--teal-dark); display: flex; align-items: center; gap: 8px; }
  .back-services .sep { width: 13px; height: 13px; border-radius: 50%; background: var(--teal-dark); }

  .coupon { left: 592px; top: 22px; width: 225px; height: 122px; border: 2px dashed var(--blue-band); background: var(--coupon-fill); text-align: center; }
  .coupon__title { background: var(--blue-band); height: 38px; line-height: 38px; font-family: "Alfa Slab One", Georgia, serif; font-size: 24px; color: var(--coupon-title); }
  .coupon__deal { margin-top: 3px; font-family: "Alfa Slab One", Georgia, serif; font-size: 20px; color: var(--coupon-teal); }
  .coupon__note { margin-top: 2px; font-size: 15px; font-style: italic; color: var(--ink-soft); line-height: 21px; }

  .gallery { left: 35px; top: 176px; width: 470px; height: 296px; }
  .shot { position: absolute; }
  .shot--before { left: 0; top: 0; width: 230px; height: 181px; background: linear-gradient(180deg, #6e7a63, #8b917a 60%, #4c5a3c); }
  .shot--after { left: 232px; top: 0; width: 238px; height: 181px; background: linear-gradient(180deg, #d8dde2, #c7ccc6 60%, #6d6a58); }
  .shot--decks { left: 0; top: 181px; width: 153px; height: 115px; background: linear-gradient(180deg, #4a6a3e, #9b6642 50%, #b0774c); }
  .shot--siding { left: 159px; top: 181px; width: 153px; height: 115px; background: linear-gradient(180deg, #e8ecef, #d2d7da 55%, #3f7a2e); }
  .shot--patios { left: 319px; top: 181px; width: 151px; height: 115px; background: linear-gradient(180deg, #3c6a55, #c08450 55%, #cf9258); }
  .band { position: absolute; background: var(--blue-band); color: #fff; height: 26px; line-height: 26px; }
  .band--before { left: 0; top: 20px; width: 150px; padding-left: 40px; font-style: italic; font-weight: 700; font-size: 19px; }
  .band--after { right: 0; top: 20px; width: 150px; text-align: center; font-style: italic; font-weight: 700; font-size: 19px; }
  .band--cat { left: 0; right: 0; top: 52px; text-align: center; font-family: "Oswald", Arial, sans-serif; font-size: 19px; color: var(--label-yellow); }
</style>
</head>
<body>

<section class="card card--front" aria-label="Postcard front">
  <div class="abs brand front-brand"><span class="brand__dot"></span>Bluestone Haven</div>
  <p class="abs front-web">WWW.BLUESTONEHAVENGROUP.COM</p>
  <p class="abs front-phone">(215) 555-0148</p>
  <p class="abs front-call">Call us today!</p>
  <p class="abs front-areas">Serving Montgomery, Bucks, Chester, Delaware,<br>&amp; Philadelphia Counties for Over 10 Years!</p>

  <div class="abs house-photo" role="img" aria-label="Photo of a large white two-storey house with black shutters on a green lawn"></div>

  <h2 class="abs services-title">Pressure Washing</h2>
  <ul class="abs services-list">
    <li>Homes</li>
    <li>Commercial Buildings</li>
    <li>Fleet Washes</li>
    <li>Apartments</li>
    <li>Drive Thrus</li>
    <li>Sidewalks</li>
    <li class="more">and more!</li>
  </ul>

  <p class="abs tagline">Beautify your home with a power wash!</p>
</section>

<section class="card card--back" aria-label="Postcard back">
  <div class="abs brand back-brand"><span class="brand__dot"></span>Bluestone Haven</div>
  <p class="abs back-web">WWW.BLUESTONEHAVENGROUP.COM</p>
  <p class="abs back-phone">(215) 555-0148</p>
  <p class="abs back-call">CALL US TODAY!</p>
  <p class="abs back-services">PRESSURE WASHING <span class="sep"></span> AIR DUCT CLEANING <span class="sep"></span> DRYER VENT CLEANING</p>

  <div class="abs coupon">
    <div class="coupon__title">COUPON</div>
    <div class="coupon__deal">$50.00 off</div>
    <div class="coupon__note">any pressure<br>washing job</div>
  </div>

  <div class="abs gallery">
    <div class="shot shot--before" role="img" aria-label="House siding before washing, stained green">
      <span class="band band--before">BEFORE</span>
    </div>
    <div class="shot shot--after" role="img" aria-label="Same house siding after washing, clean">
      <span class="band band--after">AFTER</span>
    </div>
    <div class="shot shot--decks" role="img" aria-label="Clean wooden deck">
      <span class="band band--cat">DECKS</span>
    </div>
    <div class="shot shot--siding" role="img" aria-label="Clean white house siding">
      <span class="band band--cat">SIDING</span>
    </div>
    <div class="shot shot--patios" role="img" aria-label="Clean patio with wooden fence">
      <span class="band band--cat">PATIOS</span>
    </div>
  </div>
</section>

</body>
</html>
```